RTV CRAFTED

building services
decks
pergola
renovation
extensions
general building

Target Market(s)

middle to upper class

Industry/Entity Type

building

Contact Information for Business Card

my details 0427839152 pkharlow47@mailvane.net BLD574926

Font styles to use
Serif

Colors
00AB8E
00BBA5
67D7C9
C6EFE9
E9F9F6

Requirements
Must have
• logo on the front and details on the back
Nice to have
• sharp and clean lines

```html
<!DOCTYPE html>
<html lang="en">
<head>
<meta charset="utf-8">
<title>RTV Crafted – Business Card</title>
<link rel="stylesheet" href="https://fonts.googleapis.com/css2?family=Libre+Baskerville:wght@700&family=Poppins:wght@400;500;600;700&display=swap">
<style>
  :root {
    --teal: #43b89f;
    --teal-deep: #3aa88f;
    --ink: #111111;
    --paper: #f8f8f8;
    --paper-soft: #efefef;
    --backdrop: #ececec;
    --white: #ffffff;
  }
  * { box-sizing: border-box; margin: 0; padding: 0; }
  html, body {
    width: 1200px;
    height: 2249px;
    overflow: hidden;
    background: var(--backdrop);
  }
  .card {
    position: absolute;
    left: 181px;
    width: 839px;
    height: 480px;
    overflow: hidden;
    background: linear-gradient(160deg, var(--paper), var(--paper-soft));
    box-shadow: 0 4px 8px rgba(0,0,0,.25);
  }
  .card--front { top: 585px; }
  .card--back { top: 1185px; }

  .skyline {
    position: absolute;
    left: 0;
    bottom: 0;
    background: linear-gradient(to top, var(--teal-deep), var(--teal));
  }
  .card--front .skyline { width: 100%; height: 121px; }
  .card--back .skyline { width: 519px; height: 72px; }

  .brand-name {
    font-family: "Libre Baskerville", serif;
    font-weight: 700;
    color: var(--ink);
    white-space: nowrap;
    line-height: 1;
  }
  .card--front .brand-name {
    position: absolute;
    top: 172px;
    width: 100%;
    text-align: center;
    font-size: 76px;
  }
  .card--back .brand-name {
    position: absolute;
    left: 56px;
    top: 58px;
    font-size: 38px;
  }

  .holder {
    position: absolute;
    left: 47px;
    top: 145px;
    font-family: "Poppins", sans-serif;
  }
  .holder__name { font-size: 33px; line-height: 1.1; color: var(--ink); font-weight: 400; }
  .holder__name strong { color: var(--teal); font-weight: 600; }
  .holder__licence { font-size: 17px; line-height: 1.2; font-weight: 700; color: var(--ink); margin-left: 2px; }
  .holder__licence span { color: var(--teal); }

  .contacts { position: absolute; left: 0; top: 252px; list-style: none; font-family: "Poppins", sans-serif; }
  .contacts li { display: flex; align-items: center; height: 43px; font-size: 23px; color: var(--ink); white-space: nowrap; }
  .contacts .pill {
    width: 91px; height: 22px; margin-right: 11px;
    background: var(--teal); border-radius: 0 11px 11px 0;
    display: flex; align-items: center; justify-content: flex-end; padding-right: 18px;
  }
  .contacts svg { width: 16px; height: 16px; }

  .panel { position: absolute; inset: 0; width: 839px; height: 480px; }

  .services { position: absolute; left: 566px; top: 144px; font-family: "Poppins", sans-serif; }
  .services h2 {
    font-size: 17px; font-weight: 700; color: var(--ink);
    border-bottom: 2px solid var(--ink); padding-bottom: 2px; margin-bottom: 10px;
    display: inline-block;
  }
  .services ul { list-style: none; }
  .services li { color: var(--white); font-size: 17px; font-weight: 500; height: 33px; display: flex; align-items: center; }
  .services li::before { content: ""; width: 6px; height: 6px; border-radius: 50%; background: var(--ink); margin-right: 12px; }
</style>
</head>
<body>

<section class="card card--front">
  <h1 class="brand-name">RTV CRAFTED</h1>
  <div class="skyline" role="img" aria-label="Teal city skyline silhouette along the bottom edge"></div>
</section>

<section class="card card--back">
  <div class="skyline" role="img" aria-label="Teal city skyline silhouette along the bottom edge"></div>

  <svg class="panel" viewBox="0 0 839 480" aria-hidden="true">
    <polygon points="524,0 839,0 839,480 519,480 447,231" fill="var(--teal)"/>
    <polygon points="552,0 839,0 839,480 552,480 476,231" fill="var(--white)"/>
    <polygon points="567,0 839,0 839,480 568,480 491,231" fill="var(--teal)"/>
  </svg>

  <h1 class="brand-name">RTV CRAFTED</h1>

  <div class="holder">
    <p class="holder__name">Pk <strong>Harlow</strong></p>
    <p class="holder__licence"><span>BLD</span>574926</p>
  </div>

  <ul class="contacts">
    <li><span class="pill"><svg viewBox="0 0 16 16"><path d="M3 1.5l3 .5 1 3-1.8 1.2a8 8 0 0 0 4.6 4.6L11 9l3 1 .5 3-2 1.5C7 14 2 9 1.5 3.5z" fill="var(--ink)"/></svg></span>0427839152</li>
    <li><span class="pill"><svg viewBox="0 0 16 16"><rect x="1" y="3" width="14" height="10" fill="var(--ink)"/><path d="M1 3l7 6 7-6" stroke="var(--teal)" stroke-width="1.3" fill="none"/></svg></span>pkharlow47@mailvane.net</li>
    <li><span class="pill"><svg viewBox="0 0 16 16"><circle cx="8" cy="8" r="7" fill="var(--ink)"/><path d="M1 8h14M8 1v14M3 4h10M3 12h10" stroke="var(--teal)" stroke-width="1"/><ellipse cx="8" cy="8" rx="3" ry="7" stroke="var(--teal)" stroke-width="1" fill="none"/></svg></span>www.rtvcrafted.com</li>
  </ul>

  <div class="services">
    <h2>BUILDING SERVICES</h2>
    <ul>
      <li>DECKS</li>
      <li>PERGOLA</li>
      <li>RENOVATION</li>
      <li>EXTENSIONS</li>
      <li>GENERAL BUILDING</li>
    </ul>
  </div>
</section>

</body>
</html>
```